Brindlecove Partners needs a business card design

We need a new business card design using the logo recently selected in a logo competition on Pixel Arena. Our business is a consultancy specializing in aviation and energy and the winning business card design will promote an image of precision and professionalism with creativity.

Please use the logo with the name on the front of the card and use a complementary font. Make the back white with either the light grey or dark grey logo.

Target Market(s)

Senior finance and legal leaders at aviation and energy companies

Industry/Entity Type

Management Consulting

Contact Information for Business Card

Peter Dunstable
President
Brindlecove Partners

www.brindlecovepartners.example

(713) 555-0147
pd@brindlecovepartners.example

Requirements
Must have
• Professional font that goes well with the logo font

```html
<!DOCTYPE html>
<html lang="en">
<head>
<meta charset="utf-8">
<title>Brindlecove Partners — Business Card</title>
<link href="https://fonts.googleapis.com/css2?family=Michroma&family=Montserrat:wght@400;500&display=swap" rel="stylesheet">
<style>
  :root {
    --page: #d9d9d6;
    --card: #ececea;
    --card-back: #f1f1ef;
    --navy: #17467e;
    --grey-dark: #606060;
    --grey-mid: #9b9b9b;
    --grey-text: #707070;
    --rule: #a8a8a8;
  }
  * { box-sizing: border-box; margin: 0; padding: 0; }
  html, body { width: 1200px; height: 1200px; overflow: hidden; }
  body {
    background: var(--page);
    font-family: "Montserrat", Arial, sans-serif;
    display: flex;
    flex-direction: column;
    align-items: center;
    justify-content: center;
    gap: 60px;
  }
  .card {
    position: relative;
    width: 880px;
    height: 503px;
    overflow: hidden;
    box-shadow: 0 6px 18px rgba(0,0,0,.18);
  }
  /* Back */
  .card--back { background: var(--card-back); }
  .back__name {
    position: absolute;
    left: 0; right: 0; top: 170px;
    text-align: center;
    font-family: "Michroma", Arial, sans-serif;
    font-size: 44px;
    letter-spacing: 4px;
    color: var(--grey-dark);
  }
  .back__url {
    position: absolute;
    left: 0; right: 0; top: 330px;
    text-align: center;
    font-size: 15px;
    letter-spacing: 9px;
    color: var(--grey-dark);
  }
  /* Front */
  .card--front { background: var(--card); }
  .front__bands { position: absolute; left: 0; bottom: 0; }
  .front__name-block { position: absolute; left: 38px; top: 36px; }
  .person__name {
    font-family: "Michroma", Arial, sans-serif;
    font-size: 22px;
    color: var(--navy);
    letter-spacing: 1px;
  }
  .person__title, .person__company {
    font-size: 13px;
    color: var(--grey-text);
    letter-spacing: 1px;
    margin-top: 6px;
    text-transform: uppercase;
  }
  .contact {
    position: absolute;
    display: flex;
    align-items: center;
    gap: 12px;
    font-size: 15px;
    letter-spacing: 1.5px;
    color: var(--grey-dark);
    text-transform: uppercase;
  }
  .contact svg { flex: none; }
  .contact--phone { left: 38px; top: 152px; }
  .contact--email { left: 38px; top: 238px; }
  .contact--web { left: 470px; top: 238px; }
  .front__rule {
    position: absolute;
    left: 38px; right: 38px; top: 210px;
    height: 1px;
    background: var(--rule);
  }
  .brand {
    position: absolute;
    right: 48px; top: 58px;
    text-align: right;
    font-family: "Michroma", Arial, sans-serif;
    font-size: 30px;
    letter-spacing: 2px;
    color: var(--navy);
    line-height: 1.3;
  }
</style>
</head>
<body>

  <section class="card card--back" aria-label="Card back">
    <p class="back__name">BRINDLECOVE PARTNERS</p>
    <p class="back__url">WWW.BRINDLECOVEPARTNERS.EXAMPLE</p>
  </section>

  <section class="card card--front" aria-label="Card front">
    <div class="front__name-block">
      <p class="person__name">PETER DUNSTABLE</p>
      <p class="person__title">President</p>
      <p class="person__company">Brindlecove Partners</p>
    </div>

    <p class="contact contact--phone">
      <svg width="18" height="16" viewBox="0 0 18 16" aria-hidden="true">
        <path d="M1 5 Q9 -1 17 5 L14 7 L12 5 H6 L4 7 Z" fill="var(--navy)"/>
        <rect x="3" y="8" width="12" height="7" rx="1.5" fill="var(--navy)"/>
      </svg>
      (713) 555-0147
    </p>

    <div class="front__rule"></div>

    <p class="contact contact--email">
      <svg width="20" height="14" viewBox="0 0 20 14" aria-hidden="true">
        <rect x="1" y="1" width="18" height="12" fill="none" stroke="var(--navy)" stroke-width="1.6"/>
        <path d="M1 1 L10 8 L19 1" fill="none" stroke="var(--navy)" stroke-width="1.6"/>
      </svg>
      pd@brindlecovepartners.example
    </p>

    <p class="contact contact--web">
      <svg width="18" height="18" viewBox="0 0 18 18" aria-hidden="true">
        <circle cx="9" cy="9" r="8" fill="none" stroke="var(--navy)" stroke-width="1.5"/>
        <ellipse cx="9" cy="9" rx="3.5" ry="8" fill="none" stroke="var(--navy)" stroke-width="1.2"/>
        <path d="M1 9 H17 M2.5 5 H15.5 M2.5 13 H15.5" stroke="var(--navy)" stroke-width="1.2"/>
      </svg>
      www.brindlecovepartners.example
    </p>

    <p class="brand">BRINDLECOVE<br>PARTNERS</p>

    <svg class="front__bands" width="880" height="80" viewBox="0 0 880 80" aria-hidden="true">
      <polygon points="0,20 520,20 560,80 0,80" fill="var(--navy)"/>
      <polygon points="600,20 880,20 880,80 640,80" fill="var(--grey-mid)"/>
    </svg>
  </section>

</body>
</html>
```